New landing page

We have an existing design at www.hostcorvel.com but we are not set on that design and probably want something different.
We want to increase conversion rates and experiment with a new landing page for our brightlisting promos campains.
We want to use a more single page long design page that contains these elements on one page:

Header
Images/headline
4 offer boxes
Features
Locations (map)
Testimonials
Why HostCorvel
Footer menu

Note should also be taken of research done by Pagetrove like this:
http://pagetrove.com/landing-page-articles/the-anatomy-of-a-landing-page/

Industry/Entity Type

Brightlisting

```html
<!DOCTYPE html>
<html lang="en">
<head>
<meta charset="utf-8">
<title>HostCorvel – Linux VPS Hosting</title>
<link rel="stylesheet" href="https://fonts.googleapis.com/css2?family=Oswald:wght@400;500;600&family=Roboto+Condensed:wght@400;700&family=Open+Sans:ital,wght@0,400;0,600;0,700;1,400&display=swap">
<style>
:root{
  --yellow:#f7b500;
  --yellow-dark:#d99a00;
  --black:#0a0a0a;
  --ink:#141414;
  --panel:#1c1c1c;
  --strip:#2a2a2a;
  --white:#ffffff;
  --grey-text:#bdbdbd;
  --card-top:#e9e9e9;
  --card-bottom:#c9c9c9;
  --card-head:#bdbdbd;
  --map-land:#e9e5dc;
  --map-water:#aacbe0;
}
*{margin:0;padding:0;box-sizing:border-box}
html,body{width:1200px;height:2677px;overflow:hidden}
body{position:relative;background:var(--black);color:var(--white);font-family:"Open Sans",Arial,sans-serif}
.abs{position:absolute}
ul{list-style:none}

/* backdrop */
.hero-backdrop{left:0;top:0;width:1200px;height:1463px;
  background:radial-gradient(ellipse at 50% 30%,#2a2a2a 0%,#141414 45%,#060606 100%)}

/* top bar */
.topbar-phone{left:134px;top:36px;display:flex;align-items:center;gap:12px;font-family:"Roboto Condensed",sans-serif;font-size:19px}
.topbar-phone .icon{width:26px;height:26px;border-radius:50%;background:#3a3a3a;display:flex;align-items:center;justify-content:center}
.brand{left:470px;top:24px;display:flex;align-items:center;gap:14px}
.brand .dot{width:44px;height:44px;border-radius:50%;background:var(--yellow)}
.brand .name{font-family:"Oswald",sans-serif;font-weight:500;font-size:40px;color:var(--white);letter-spacing:1px}
.account-btn{left:955px;top:33px;width:111px;height:29px;background:var(--yellow);color:var(--black);
  font-family:"Roboto Condensed",sans-serif;font-weight:700;font-size:16px;display:flex;align-items:center;justify-content:center}

.main-nav{left:0;top:90px;width:1200px;height:40px;background:#050505;border-bottom:1px solid #2b2b2b}
.main-nav ul{position:absolute;left:134px;width:932px;top:0;height:40px;display:flex;justify-content:space-between;align-items:center}
.main-nav a{color:var(--white);text-decoration:none;font-family:"Roboto Condensed",sans-serif;font-size:17px;padding:9px 0}
.main-nav a.active{border-bottom:3px solid var(--white)}

/* hero */
.hero-title{left:134px;top:170px;font-family:"Oswald",sans-serif;line-height:1}
.hero-title .pre{font-size:32px;font-weight:500;display:block}
.hero-title .main{font-size:37px;font-weight:500;color:var(--yellow);display:block;margin-top:6px}
.hero-title .main b{font-size:46px;font-weight:600}
.checklist{left:134px;top:277px;width:390px;height:231px;background:rgba(20,20,20,.88);padding:22px 0 0 22px}
.checklist li{display:flex;align-items:center;gap:20px;height:41.5px;font-size:15.5px;color:#e8e8e8}
.hosting-btn{left:134px;top:540px;width:156px;height:36px;background:var(--yellow);color:var(--black);
  font-family:"Oswald",sans-serif;font-weight:500;font-size:20px;display:flex;align-items:center;justify-content:center}
.server-visual{left:620px;top:262px;width:400px;height:300px;border-radius:30px;
  background:linear-gradient(180deg,#f2f2f2 0%,#cfcfcf 55%,#9c9c9c 100%)}
.hero-arrow{left:585px;top:178px}
.price-cloud{left:675px;top:170px}
.price-cloud-text{left:675px;top:170px;width:145px;height:76px;display:flex;align-items:flex-end;justify-content:center;padding-bottom:12px;
  font-family:"Oswald",sans-serif;font-size:19px}
.price-cloud-text b{font-size:32px;color:var(--white);font-weight:500;margin-left:6px;line-height:.9}
.per-month{left:832px;top:215px;font-family:"Roboto Condensed",sans-serif;font-weight:700;font-size:14px}
.promo{left:505px;top:604px;font-family:"Oswald",sans-serif;font-size:21px;white-space:nowrap}
.promo span{font-family:"Roboto Condensed",sans-serif;font-size:18.5px;color:var(--yellow)}
.promo span em{font-style:normal;color:var(--yellow)}

/* pricing */
.plan{top:687px;width:212px;height:417px;background:linear-gradient(180deg,var(--card-top),var(--card-bottom));
  box-shadow:8px 0 0 #8e8e8e;color:#141414;text-align:center;font-family:"Roboto Condensed",sans-serif}
.plan-name{height:76px;background:linear-gradient(180deg,#d6d6d6,#bfbfbf);display:flex;align-items:center;justify-content:center;
  font-family:"Oswald",sans-serif;font-size:25px;font-weight:500}
.plan-price{position:relative;height:90px;margin-top:10px}
.plan-price svg{position:absolute;left:36px;top:0}
.plan-price .amount{position:absolute;left:36px;top:16px;width:140px;text-align:center;font-family:"Oswald",sans-serif;font-size:30px;color:var(--yellow)}
.plan-price .amount small{font-size:14px}
.plan-ram{font-weight:700;font-size:18px;margin-top:8px}
.plan-specs{font-size:14px;line-height:24px;margin-top:12px;color:#333}
.plan-activation{font-weight:700;font-size:17px;margin-top:14px}
.order-btn{position:absolute;left:18px;top:350px;width:163px;height:44px;background:var(--yellow);
  box-shadow:6px 6px 0 var(--yellow-dark);font-family:"Oswald",sans-serif;font-size:20px;font-weight:500;display:flex;align-items:center;justify-content:center}

/* features */
.features-title{left:134px;top:1153px;width:932px;height:60px;background:#1f1f1f;display:flex;align-items:center;justify-content:center;
  font-family:"Oswald",sans-serif;font-size:37px}
.features-title span{color:var(--yellow)}
.feature{top:1258px;width:240px;text-align:center}
.feature svg{display:block;margin:0 auto}
.feature p{font-family:"Roboto Condensed",sans-serif;font-size:19px;margin-top:36px}
.slide-arrow{top:1333px}

/* map */
.map-area{left:0;top:1463px;width:1200px;height:261px;
  background:linear-gradient(100deg,var(--map-water) 0%,#c9dbe6 12%,var(--map-land) 22%,#ece8de 60%,#e3dfd4 100%)}
.location-card{left:138px;top:1503px;width:413px;height:187px;background:#161616;border-radius:4px;padding:18px 24px;font-size:16px}
.location-card .arrow{position:absolute;right:-16px;top:80px;width:0;height:0;border-top:16px solid transparent;border-bottom:16px solid transparent;border-left:16px solid #161616}
.location-row{display:flex;gap:16px;align-items:flex-start}
.location-row .ic{width:20px;flex:none;display:flex;justify-content:center;padding-top:3px}
.location-name{font-weight:700;font-size:17px}
.location-addr{margin-left:46px;line-height:21px;color:#e5e5e5;font-size:15px}
.location-row.small{margin-top:10px;font-weight:700;font-size:15px}

/* testimonials */
.testimonial-bg{left:0;top:1724px;width:1200px;height:301px;background:linear-gradient(180deg,#2d2d2d,#1e1e1e)}
.testimonial-title{left:0;top:1755px;width:1200px;text-align:center;font-family:"Oswald",sans-serif;font-size:38px}
.avatar{left:152px;top:1829px;width:138px;height:138px;border-radius:50%;border:5px solid #eee;background:linear-gradient(180deg,#c9ced4,#8e959c)}
.quote-box{left:305px;top:1833px;width:750px;height:123px;background:#e4e4e4;border-radius:4px;color:#222;padding:14px 18px 0 40px;
  font-size:12.4px;font-style:italic;line-height:21px}
.quote-box::before{content:"";position:absolute;left:-14px;top:44px;border-top:14px solid transparent;border-bottom:14px solid transparent;border-right:14px solid #e4e4e4}
.quote-mark{position:absolute;left:14px;top:2px;font-family:"Oswald",sans-serif;font-size:48px;color:#999;font-style:normal}
.quote-author{left:305px;top:1974px;font-size:12px;font-style:italic;font-weight:600}
.slider-dots{left:975px;top:1972px;display:flex;gap:5px}
.slider-dots i{width:14px;height:14px;border-radius:50%;background:#fff}
.slider-dots i.on{background:var(--yellow)}
.why-rule{left:0;top:2025px;width:1200px;height:3px;background:var(--yellow)}

/* why */
.why-bg{left:0;top:2028px;width:1200px;height:298px;background:var(--ink)}
.why-title{left:134px;top:2056px;font-family:"Oswald",sans-serif;font-size:37px;font-weight:500}
.why-title span{color:var(--yellow)}
.why-list{left:134px;top:2112px}
.why-list li{display:flex;align-items:center;gap:14px;height:38px;font-size:15px}
.server-rack{left:780px;top:2103px;width:357px;height:201px;background:linear-gradient(180deg,#dcdcdc,#8f8f8f);border-radius:4px}

/* partners */
.partners{left:0;top:2326px;width:1200px;height:76px;background:var(--strip);display:flex;align-items:center}
.partner-mark{position:absolute;top:20px;height:36px;background:#4a4a4a}

/* footer */
.footer{left:0;top:2402px;width:1200px;height:234px;background:#111}
.footer-col{top:2420px;width:230px}
.footer-col h4{font-family:"Oswald",sans-serif;font-weight:400;font-size:21px;letter-spacing:.5px}
.footer-col h4 span{font-weight:600;color:var(--white)}
.footer-col ul{margin-top:18px}
.footer-col li{font-size:13px;line-height:23.5px;color:#e2e2e2;display:flex;align-items:center;gap:10px}
.footer-col li::before{content:"";width:5px;height:5px;border-top:2px solid var(--yellow);border-right:2px solid var(--yellow);transform:rotate(45deg)}
.newsletter p{font-size:13px;line-height:20px;color:#e2e2e2;margin-top:18px;width:210px}
.newsletter .field{margin-top:12px;width:203px;height:29px;background:#fff;color:#444;font-size:12px;padding:6px 7px}
.newsletter .submit{margin-top:18px;width:74px;height:27px;border:1px solid #888;font-size:12px;display:flex;align-items:center;justify-content:center}
.bottom-bar{left:0;top:2636px;width:1200px;height:41px;background:var(--yellow);}
.copyright{left:134px;top:2646px;font-size:12.5px;color:#141414}
.social{top:2643px;width:24px;height:24px;border-radius:50%;background:#141414}
</style>
</head>
<body>

<svg width="0" height="0" style="position:absolute">
  <defs>
    <symbol id="cloud" viewBox="0 0 220 130">
      <path d="M48 122 H172 C200 122 215 100 210 78 C206 58 190 48 176 50 C170 24 148 8 120 8 C92 8 72 26 68 46 C50 42 30 54 28 74 C14 80 10 96 16 108 C22 118 34 122 48 122 Z"/>
    </symbol>
    <symbol id="tick" viewBox="0 0 24 20">
      <path d="M2 10 L9 17 L22 3" fill="none" stroke="currentColor" stroke-width="3"/>
    </symbol>
  </defs>
</svg>

<div class="abs hero-backdrop" role="img" aria-label="Dark server room aisle with racks of blinking servers"></div>

<header>
  <div class="abs topbar-phone">
    <span class="icon"><svg width="14" height="14" viewBox="0 0 24 24"><path d="M6 2 L10 6 L8 9 C9 12 12 15 15 16 L18 14 L22 18 L19 22 C10 21 3 14 2 5 Z" fill="#fff"/></svg></span>
    +1 800 555 0147
  </div>
  <div class="abs brand"><span class="dot"></span><span class="name">HostCorvel</span></div>
  <a class="abs account-btn">MY ACCOUNT</a>
  <nav class="abs main-nav">
    <ul>
      <li><a class="active">HOME</a></li><li><a>ABOUT</a></li><li><a>SERVICES</a></li><li><a>FEATURES</a></li>
      <li><a>LOCATION</a></li><li><a>FAQ</a></li><li><a>PAYMENT METHODS</a></li><li><a>COMMUNITY</a></li>
      <li><a>SUPPORT</a></li><li><a>CONTACT</a></li>
    </ul>
  </nav>
</header>

<section class="hero">
  <h1 class="abs hero-title"><span class="pre">YOUR OWN</span><span class="main">Linux Server in <b>59</b> seconds</span></h1>
  <ul class="abs checklist">
    <li><svg width="22" height="18" style="color:var(--yellow)"><use href="#tick"/></svg>Lorem ipsum dolor sit amet Fusce males</li>
    <li><svg width="22" height="18" style="color:var(--yellow)"><use href="#tick"/></svg>Fusce malesuada velit etionli sagittis facili</li>
    <li><svg width="22" height="18" style="color:var(--yellow)"><use href="#tick"/></svg>Nulla pulvinar sagittis faciliFusce</li>
    <li><svg width="22" height="18" style="color:var(--yellow)"><use href="#tick"/></svg>Vivamus posuere justo eu eli</li>
    <li><svg width="22" height="18" style="color:var(--yellow)"><use href="#tick"/></svg>Fusce malesuada velit etionli sagittis facili</li>
  </ul>
  <a class="abs hosting-btn">HOSTING PLAN</a>

  <div class="abs server-visual" role="img" aria-label="Silver server box with a cloud emblem on its lid"></div>
  <svg class="abs hero-arrow" width="80" height="60" viewBox="0 0 80 60"><path d="M6 54 C10 30 30 16 62 14" fill="none" stroke="#fff" stroke-width="4"/><path d="M52 4 L68 14 L54 26" fill="none" stroke="#fff" stroke-width="4"/></svg>
  <svg class="abs price-cloud" width="145" height="86" viewBox="0 0 220 130"><use href="#cloud" fill="#0a0a0a" stroke="#fff" stroke-width="4"/></svg>
  <div class="abs price-cloud-text">Only <b style="color:var(--yellow)">$99</b></div>
  <div class="abs per-month">per month</div>

  <p class="abs promo">CURRENT PROMOTION: <span>Free SSL certificate and .com domain on <em>VIP CtrlDeck Managed VPS</em></span></p>
</section>

<section class="pricing">
  <article class="abs plan" style="left:134px">
    <h3 class="plan-name">BUDGET VPS</h3>
    <div class="plan-price"><svg width="140" height="84" viewBox="0 0 220 130"><use href="#cloud" fill="#111"/></svg><span class="amount">$10.00<small> /mo</small></span></div>
    <p class="plan-ram">256 MB Guaranteed RAM</p>
    <p class="plan-specs">1x 3.4 Ghz Cores<br>10 GB Raid-10 Storage<br>300 GB Bandwidth</p>
    <p class="plan-activation">59 second Activation</p>
    <a class="order-btn">ORDER NOW</a>
  </article>
  <article class="abs plan" style="left:372px">
    <h3 class="plan-name">CUSTOM VPS</h3>
    <div class="plan-price"><svg width="140" height="84" viewBox="0 0 220 130"><use href="#cloud" fill="#111"/></svg><span class="amount">$10.00<small> /mo</small></span></div>
    <p class="plan-ram">Customize your RAM</p>
    <p class="plan-specs">Customize CPU<br>Customize Storage<br>Customize Bandwidth</p>
    <p class="plan-activation">59 second Activation</p>
    <a class="order-btn">ORDER NOW</a>
  </article>
  <article class="abs plan" style="left:611px">
    <h3 class="plan-name">EXTREME VPS</h3>
    <div class="plan-price"><svg width="140" height="84" viewBox="0 0 220 130"><use href="#cloud" fill="#111"/></svg><span class="amount">$40.00<small> /mo</small></span></div>
    <p class="plan-ram">2048 MB Guaranteed RAM</p>
    <p class="plan-specs">4x 3.4 Ghz Cores<br>100 GB Raid-10 Storage<br>3000 GB Bandwidth</p>
    <p class="plan-activation">59 second Activation</p>
    <a class="order-btn">ORDER NOW</a>
  </article>
  <article class="abs plan" style="left:850px">
    <h3 class="plan-name">CTRLDECK VPS</h3>
    <div class="plan-price"><svg width="140" height="84" viewBox="0 0 220 130"><use href="#cloud" fill="#111"/></svg><span class="amount">$45.00<small> /mo</small></span></div>
    <p class="plan-ram">1024 MB Guaranteed RAM</p>
    <p class="plan-specs">Customize CPU<br>Customize Storage<br>Customize Bandwidth</p>
    <p class="plan-activation">59 second Activation</p>
    <a class="order-btn">ORDER NOW</a>
  </article>
</section>

<section class="features">
  <h2 class="abs features-title"><span>VPS</span>&nbsp;HOSTING FEATURES</h2>
  <svg class="abs slide-arrow" style="left:86px" width="16" height="24" viewBox="0 0 16 24"><path d="M13 2 L3 12 L13 22" fill="none" stroke="#888" stroke-width="3"/></svg>
  <svg class="abs slide-arrow" style="left:1106px" width="16" height="24" viewBox="0 0 16 24"><path d="M3 2 L13 12 L3 22" fill="none" stroke="#888" stroke-width="3"/></svg>

  <div class="abs feature" style="left:121px">
    <svg width="200" height="115" viewBox="0 0 220 130"><use href="#cloud" fill="#0a0a0a" stroke="var(--yellow)" stroke-width="5"/>
      <circle cx="112" cy="72" r="20" fill="none" stroke="#fff" stroke-width="5"/><path d="M112 60 V72 H122" fill="none" stroke="#fff" stroke-width="4"/></svg>
    <p>59 Second Activation</p>
  </div>
  <div class="abs feature" style="left:364px">
    <svg width="200" height="115" viewBox="0 0 220 130"><use href="#cloud" fill="#0a0a0a" stroke="var(--yellow)" stroke-width="5"/>
      <rect x="101" y="46" width="20" height="14" fill="#fff"/><rect x="82" y="76" width="20" height="14" fill="#fff"/><rect x="120" y="76" width="20" height="14" fill="#fff"/>
      <path d="M111 60 V68 M92 68 H130 M92 68 V76 M130 68 V76" stroke="#fff" stroke-width="2" fill="none"/></svg>
    <p>99.9% Uptime</p>
  </div>
  <div class="abs feature" style="left:596px">
    <svg width="200" height="115" viewBox="0 0 220 130"><use href="#cloud" fill="#0a0a0a" stroke="var(--yellow)" stroke-width="5"/>
      <circle cx="112" cy="70" r="22" fill="none" stroke="#fff" stroke-width="4" stroke-dasharray="6 3"/><circle cx="112" cy="70" r="14" fill="#fff"/>
      <path d="M105 70 L110 75 L119 65" fill="none" stroke="#0a0a0a" stroke-width="3"/></svg>
    <p>14 Day Moneyback Guarantee</p>
  </div>
  <div class="abs feature" style="left:837px">
    <svg width="200" height="115" viewBox="0 0 220 130"><use href="#cloud" fill="#0a0a0a" stroke="var(--yellow)" stroke-width="5"/>
      <circle cx="112" cy="72" r="20" fill="none" stroke="#fff" stroke-width="4"/><path d="M112 60 V82 M104 74 L112 82 L120 74" fill="none" stroke="#fff" stroke-width="4"/></svg>
    <p>Full Root Access</p>
  </div>
</section>

<section class="location">
  <div class="abs map-area" role="img" aria-label="Street map of the area around the office with roads and a coastline"></div>
  <div class="abs location-card">
    <span class="arrow"></span>
    <div class="location-row">
      <span class="ic"><svg width="14" height="20" viewBox="0 0 14 20"><path d="M7 0 C3 0 0 3 0 7 C0 12 7 20 7 20 C7 20 14 12 14 7 C14 3 11 0 7 0 Z" fill="#fff"/><circle cx="7" cy="7" r="2.5" fill="#161616"/></svg></span>
      <span class="location-name">Larkfield Limited Trading As HostCorvel</span>
    </div>
    <p class="location-addr">41 Alder Crest Rd<br>Wellington<br>New Zealand</p>
    <div class="location-row small">
      <span class="ic"><svg width="16" height="16" viewBox="0 0 24 24"><path d="M6 2 L10 6 L8 9 C9 12 12 15 15 16 L18 14 L22 18 L19 22 C10 21 3 14 2 5 Z" fill="#fff"/></svg></span>+1 800 555 0147
    </div>
    <div class="location-row small">
      <span class="ic"><svg width="16" height="12" viewBox="0 0 16 12"><rect width="16" height="12" fill="#fff"/><path d="M0 0 L8 7 L16 0" fill="none" stroke="#161616" stroke-width="1.5"/></svg></span>support@hostcorvel.com
    </div>
  </div>
</section>

<section class="testimonials">
  <div class="abs testimonial-bg" role="img" aria-label="Dimmed server room backdrop"></div>
  <h2 class="abs testimonial-title">WHAT OUR CUSTOMERS ARE SAYING</h2>
  <div class="abs avatar" role="img" aria-label="Customer portrait"></div>
  <blockquote class="abs quote-box">
    <span class="quote-mark">&ldquo;</span>
    Lorem ipsum dolor sit amet, consectetuer adipiscing elit, sed diam nonummy nibh euismod tincidunt ut laoreet dolore magna aliquam erat volutpat. Ut wisi enim ad minim veniam, quis nostrud exerci tation ullamcorper suscipit lobortis nisl ut aliquip commodo consequat. Duis autem vel eum iriure dolor in hendrerit in vulputate velit esse molestie consequat, vel illum dolore eu feugiat nulla facilisis at vero eros et accumsan et iusto odio dignissimqui duis dolore te feugait nulla facilisi.
  </blockquote>
  <p class="abs quote-author">... Marek, Driftline Networks , USA</p>
  <div class="abs slider-dots"><i class="on"></i><i></i><i></i><i></i><i></i></div>
</section>

<div class="abs why-rule"></div>
<section class="why">
  <div class="abs why-bg"></div>
  <h2 class="abs why-title">WHY <span>HOSTCORVEL</span></h2>
  <ul class="abs why-list">
    <li><svg width="18" height="15" style="color:#fff"><use href="#tick"/></svg>Neque porro quisquam est, qui dolorem ipsum quia dolor sit amet, consectetur, adipisci</li>
    <li><svg width="18" height="15" style="color:#fff"><use href="#tick"/></svg>aliquam quaerat voluptatem. Ut enim ad minima veniam</li>
    <li><svg width="18" height="15" style="color:#fff"><use href="#tick"/></svg>Neque porro quisquam est, qui dolorem ipsum quia dolor sit amet</li>
    <li><svg width="18" height="15" style="color:#fff"><use href="#tick"/></svg>aliquam quaerat voluptatem. Ut enim ad minima veniam ipsum quia dolor sit amet</li>
    <li><svg width="18" height="15" style="color:#fff"><use href="#tick"/></svg>Neque porro quisquam est, qui dolorem ipsum quia dolor sit amet</li>
  </ul>
  <div class="abs server-rack" role="img" aria-label="Stack of rack-mounted servers lit from above"></div>
</section>

<section class="abs partners" aria-label="Technology partners">
  <span class="partner-mark" style="left:140px;width:86px;border-radius:18px"></span>
  <span class="partner-mark" style="left:275px;width:84px"></span>
  <span class="partner-mark" style="left:397px;width:84px;border-radius:18px"></span>
  <span class="partner-mark" style="left:530px;width:100px"></span>
  <span class="partner-mark" style="left:703px;width:52px;border-radius:50%;height:36px"></span>
  <span class="partner-mark" style="left:815px;width:88px"></span>
  <span class="partner-mark" style="left:955px;width:88px;border-radius:18px"></span>
</section>

<footer>
  <div class="abs footer"></div>
  <div class="abs footer-col" style="left:132px">
    <h4>SERVICES</h4>
    <ul><li>Budget Linux VPS</li><li>Standard Linux VPS</li><li>Extreme Linux VPS</li><li>Managed CtrlDeck VPS</li><li>Custom Linux VPS</li><li>Domains and SSL certs</li></ul>
  </div>
  <div class="abs footer-col" style="left:375px">
    <h4>COMPANY</h4>
    <ul><li>VPS F.A.Q</li><li>Terms of service</li><li>Acceptable Use Policy</li><li>Privacy Policy</li><li>Security</li><li>About Us</li></ul>
  </div>
  <div class="abs footer-col" style="left:618px">
    <h4>SUPPORT</h4>
    <ul><li>Billing Login</li><li>Support Center</li><li>Knowledgebase</li><li>Contact Us</li><li>Submit a Ticket</li></ul>
  </div>
  <div class="abs footer-col newsletter" style="left:863px">
    <h4>LEAVE US A <span>MESSAGE</span></h4>
    <p>Lorem ipsum dolo consectetuer Ut enim ad minim veniauis.</p>
    <div class="field">Email Address</div>
    <div class="submit">SUBMIT</div>
  </div>
  <div class="abs bottom-bar"></div>
  <p class="abs copyright">© Copyright 2014 HostCorvel A division of Larkfield Limited.  All Rights Reserved.</p>
  <span class="abs social" style="left:947px"></span>
  <span class="abs social" style="left:977px"></span>
  <span class="abs social" style="left:1007px"></span>
  <span class="abs social" style="left:1041px"></span>
</footer>

</body>
</html>
```